Gentleman's grooming products require a business card

I need a business card that incorporates the logo [ or parts of ] that we had Pixel Hive design for us as uploaded.

We sell online, mens grooming products including moustache waxes, beard oils and shaving accessories.
We want a card that is classy, professional and a card that shouts mens products.

Target Market(s)

Young professional male market

Industry/Entity Type

Business

Contact Information for Business Card

Ross and Edith Carwell
Lather and Lore
Purveyors of gentleman's stiffeners and grooming requisites
M :0418529647
E : ross@latherandlore.com.au
E : edith@latherandlore.com.au
E : sales@theblokesbalmery.com.au

W : www.latherandlore.com.au

Requirements
Must have
• Class
Nice to have
• Professionalism

```html
<!DOCTYPE html>
<html lang="en">
<head>
<meta charset="utf-8">
<title>Lather and Lore — Business Card</title>
<link rel="stylesheet" href="https://fonts.googleapis.com/css2?family=Open+Sans:wght@400;700&display=swap">
<style>
  :root {
    --backdrop: #2a2623;
    --card: #0d0d0d;
    --card-sheen: #1c1c1c;
    --ink: #f2f2f2;
    --ink-soft: #c9c9c9;
    --rule: #d8d8d8;
  }
  * { box-sizing: border-box; margin: 0; padding: 0; }
  html, body {
    width: 1200px; height: 1023px; overflow: hidden;
    background: var(--backdrop);
    font-family: "Open Sans", Arial, sans-serif;
  }
  .canvas {
    width: 1200px; height: 1023px;
    display: flex; align-items: center; justify-content: center;
  }
  .card {
    position: relative;
    width: 1000px; height: 572px;
    background: linear-gradient(160deg, var(--card-sheen) 0%, var(--card) 45%, var(--card) 100%);
    color: var(--ink);
    box-shadow: 0 20px 50px rgba(0,0,0,.5);
  }
  .brand {
    position: absolute; right: 90px; top: 70px;
    display: flex; align-items: center; gap: 22px;
  }
  .brand-mark {
    width: 64px; height: 64px;
    border: 2px solid var(--rule);
  }
  .brand-name {
    font-size: 54px; font-weight: 400; color: var(--ink);
    letter-spacing: .5px;
  }
  .tagline {
    position: absolute; right: 90px; top: 160px;
    font-size: 13px; letter-spacing: 1.6px; text-transform: uppercase;
    color: var(--ink-soft);
  }
  .rule-main {
    position: absolute; left: 90px; right: 90px; top: 205px;
    height: 2px; background: var(--rule);
  }
  .contact {
    position: absolute; left: 90px; right: 90px; top: 260px;
  }
  .contact-head {
    display: flex; align-items: flex-end; gap: 18px;
  }
  .contact-name { font-size: 34px; font-weight: 700; line-height: 1.2; white-space: nowrap; }
  .contact-rule {
    flex: 1; height: 2px; background: var(--rule); margin-bottom: 10px;
  }
  .contact-company { font-size: 22px; color: var(--ink-soft); margin-bottom: 22px; }
  .contact-list { list-style: none; }
  .contact-list li {
    display: flex; align-items: center; gap: 16px;
    font-size: 22px; line-height: 1.55; color: var(--ink);
  }
  .contact-list svg { width: 22px; height: 22px; flex: none; }
  .website {
    position: absolute; right: 90px; bottom: 60px;
    font-size: 22px; color: var(--ink-soft);
  }
</style>
</head>
<body>
<main class="canvas">
  <section class="card" aria-label="Business card for Lather and Lore">
    <div class="brand">
      <span class="brand-mark" aria-hidden="true"></span>
      <span class="brand-name">Lather and Lore</span>
    </div>
    <p class="tagline">Suppliers of fine moustache waxes and shaving essentials</p>
    <div class="rule-main"></div>

    <div class="contact">
      <div class="contact-head">
        <h1 class="contact-name">Ross and Edith Carwell</h1>
        <span class="contact-rule" aria-hidden="true"></span>
      </div>
      <p class="contact-company">Lather and Lore</p>
      <ul class="contact-list">
        <li>
          <svg viewBox="0 0 24 24" aria-hidden="true"><path fill="#f2f2f2" d="M4 8c0-2 2-4 8-4s8 2 8 4v2h-4V8H8v2H4zM7 11h10l3 8H4z"/><circle cx="12" cy="15" r="2" fill="#0d0d0d"/></svg>
          (041) 852 9647
        </li>
        <li>
          <svg viewBox="0 0 24 24" aria-hidden="true"><rect x="3" y="5" width="18" height="14" fill="none" stroke="#f2f2f2" stroke-width="2"/><path d="M3 5l9 8 9-8M3 19l7-7M21 19l-7-7" fill="none" stroke="#f2f2f2" stroke-width="2"/></svg>
          ross@latherandlore.com.au
        </li>
        <li>
          <svg viewBox="0 0 24 24" aria-hidden="true"><rect x="3" y="5" width="18" height="14" fill="none" stroke="#f2f2f2" stroke-width="2"/><path d="M3 5l9 8 9-8M3 19l7-7M21 19l-7-7" fill="none" stroke="#f2f2f2" stroke-width="2"/></svg>
          edith@latherandlore.com.au
        </li>
        <li>
          <svg viewBox="0 0 24 24" aria-hidden="true"><rect x="3" y="5" width="18" height="14" fill="none" stroke="#f2f2f2" stroke-width="2"/><path d="M3 5l9 8 9-8M3 19l7-7M21 19l-7-7" fill="none" stroke="#f2f2f2" stroke-width="2"/></svg>
          sales@theblokesbalmery.com.au
        </li>
      </ul>
    </div>

    <p class="website">www.latherandlore.com.au</p>
  </section>
</main>
</body>
</html>
```